Brochure Design Project

I need a presentation folder with two inside pages and a pocket on back cover, use use my logo ,
make the cover just using the logo (put it big and centered, then use the logo in the background to fill, read the brief and make it modern, stop trying to make it exactly like the picture I gave as sample please use your talent trust your self
I just uploaded text for presentation folder
Target Market(s)
Dr's offices and patients

```html
<!DOCTYPE html>
<html lang="en">
<head>
<meta charset="utf-8">
<title>ClearPath Counseling – Presentation Folder Inside Spread</title>
<link rel="stylesheet" href="https://fonts.googleapis.com/css2?family=Open+Sans:wght@300;400;600;700&display=swap">
<style>
  :root {
    --canvas: #ffffff;
    --page-top: #f3eddf;
    --page-mid: #e2d6bd;
    --page-bottom: #c9b28d;
    --fold-shade: rgba(120, 90, 50, 0.18);
    --brown: #5a3310;
    --text: #5c4a36;
    --text-strong: #4a2c10;
    --on-brown: #f6efe4;
  }
  * { box-sizing: border-box; margin: 0; padding: 0; }
  html, body {
    width: 1200px; height: 800px; overflow: hidden;
    background: var(--canvas);
    font-family: "Open Sans", Arial, sans-serif;
  }
  .folder-spread {
    position: absolute; left: 85px; top: 36px;
    width: 1030px; height: 704px;
    display: flex;
  }
  .page {
    position: relative; height: 100%;
    background: linear-gradient(180deg, var(--page-top) 0%, var(--page-mid) 50%, var(--page-bottom) 100%);
  }
  .page--left { width: 513px; }
  .page--right {
    width: 517px;
    background:
      linear-gradient(90deg, var(--fold-shade) 0%, rgba(0,0,0,0) 8%),
      linear-gradient(180deg, var(--page-top) 0%, var(--page-mid) 50%, var(--page-bottom) 100%);
  }

  .brand {
    position: absolute; left: 290px; top: 72px;
    display: flex; align-items: center; gap: 10px;
    color: var(--brown);
    font-size: 25px; font-weight: 600; letter-spacing: 0.2px;
  }
  .brand__dot {
    width: 34px; height: 34px; border-radius: 50%;
    background: var(--brown);
  }

  .intro {
    position: absolute; left: 228px; top: 158px; width: 250px;
    color: var(--text);
    font-size: 9.3px; font-weight: 300; line-height: 15.2px;
  }
  .intro p { margin-bottom: 15px; }
  .intro strong { color: var(--text-strong); font-weight: 700; }

  .info {
    position: absolute; left: 35px; top: 162px; width: 232px;
    color: var(--text);
    font-size: 9.3px; font-weight: 300; line-height: 15.2px;
  }
  .info__heading {
    font-size: 8.6px; font-weight: 400; letter-spacing: 0.3px;
    margin-bottom: 13px; text-transform: uppercase;
  }
  .info__list { list-style: none; margin-bottom: 32px; }
  .info__list li { position: relative; padding-left: 14px; }
  .info__list li::before {
    content: ""; position: absolute; left: 0; top: 4.5px;
    width: 6px; height: 6px; border-radius: 50%;
    background: var(--text-strong);
  }
  .info__list--square li::before { border-radius: 0; }

  .pocket {
    position: absolute; right: 0; top: 2px;
    width: 227px; height: 700px;
  }
  .pocket svg { display: block; }
  .pocket__text {
    position: absolute; left: 28px; top: 520px; width: 195px;
    color: var(--on-brown);
    font-size: 12.3px; font-weight: 400; line-height: 15px;
  }
  .pocket__text p { margin-bottom: 15px; }
</style>
</head>
<body>
  <main class="folder-spread">
    <section class="page page--left">
      <div class="brand">
        <span class="brand__dot"></span>
        <span class="brand__name">ClearPath Counseling</span>
      </div>

      <div class="intro">
        <p><strong>ClearPath Counseling</strong> is a proactive addiction counseling agency dedicated to address health issues in an integrated manner by working with Pain Management Physicians to offer opiod education to prevent substance use and misuse disorders to their Patients.</p>
        <p><strong>ClearPath Counseling</strong> is a resource for Pain Management Clinics to educate and provide prevention and counseling program to patients to reduce the risk of substance use disorders for those patients at risk to pain related substance use disorders.</p>
        <p><strong>ClearPath Counseling</strong> will provide education and prevention to individuals who are prescribed medications for health related reasons to prevent possible substance use disorders.</p>
        <p><strong>ClearPath Counseling</strong> will receive referrals from pain management clinics to address this growing issue in healthcare.</p>
        <p><strong>ClearPath Counseling</strong> services are provided by addiction professionals who are experienced in working in all areas of addiction education and prevention and care.</p>
        <p>Many Pain Management Physicians are interested in reducing risk to their patients and practice from opiod misuse and Increasing Quality Care for their Patients!</p>
        <p><strong>ClearPath Counseling</strong> will provide education services and screening to provide patients information to reduce the possible addiction potential.</p>
        <p><strong>ClearPath Counseling</strong> will provide education, prevention, screening, assessments, and referrals for those individuals with chronic pain and substance use disorders.</p>
      </div>
    </section>

    <section class="page page--right">
      <div class="info">
        <h2 class="info__heading">Services Offered</h2>
        <ul class="info__list">
          <li>Pro active opiod education</li>
          <li>Education materials to inform patients about the risk of taking medications inappropriately.</li>
          <li>Prevention services to educate patients about the risk and warning symptoms of substance misuse and abuse</li>
          <li>Screening for potential substance use disorders related to prescribed</li>
          <li>Assessment for substance use disorders related to medical issues and prescribed medications</li>
          <li>Counseling provided by experienced addiction professionals to address substance related misuse and abuse for patients taking prescribed medications.</li>
        </ul>

        <h2 class="info__heading">Opiod Education</h2>
        <ul class="info__list info__list--square">
          <li>Using Opiods safely</li>
          <li>The Role of Medications</li>
          <li>Opiod Agreements and Contracts</li>
          <li>Responsible Use</li>
          <li>Storing Medication</li>
          <li>Alcohol &amp; Marijuana and Pain Medication</li>
          <li>Over the Counter Medication</li>
          <li>Storing your Medication Safely</li>
        </ul>
      </div>

      <div class="pocket">
        <svg width="227" height="700" viewBox="0 0 227 700" aria-hidden="true">
          <path d="M0 0 H227 V700 H0 V388 A43 43 0 0 0 0 302 Z" fill="var(--brown)"/>
        </svg>
        <div class="pocket__text">
          <p>According to the Meridian Health Institute more than 76 million Americans are suffering with chronic pain.</p>
          <p>Pro Active Addiction Counseling is needed and no one is providing this service!</p>
          <p>ClearPath Counseling is !</p>
        </div>
      </div>
    </section>
  </main>
</body>
</html>
```